Homecare Design. I would like the color to be same as my business cards

Gentle Hearthkeeper & Helper Agency
I would something very light on the eyes.
Easy to read nothing complicated
I want something that demonstrate soft touch

My contact number has change cell: 203-555-0187 office: 2035550142

Target Market(s)

Elderly
people looking for someone to take care of there love ones
Target age starting at 50

Industry/Entity Type

Business

Font styles to use
Serif

Colors
3176b5
3276b5
85acd3
ceddec

Requirements
Must have

Nice to have
• I woluld like something like helping hands
Should not have
• I really don't care to see medical supplies, medication

```html
<!DOCTYPE html>
<html lang="en">
<head>
<meta charset="utf-8">
<title>Gentle Hearthkeeper &amp; Helper Agency – Postcard</title>
<link rel="stylesheet" href="https://fonts.googleapis.com/css2?family=Roboto:wght@300;400&family=Arimo:wght@400;700&family=Tinos:ital,wght@1,700&display=swap">
<style>
  :root {
    --brand-blue: #3176b5;
    --brand-blue-alt: #3276b5;
    --soft-blue: #85acd3;
    --pale-blue: #ceddec;
    --panel-grey: #f4f6f9;
    --stage: #1a1d20;
    --paper: #ffffff;
    --rule: #9a9a9a;
    --deep-blue: #1f3f9a;
    --skin-warm: #e2b9a0;
    --skin-light: #eccbb6;
    --linen: #f1f1f1;
    --stamp-grey: #707070;
  }
  * { margin: 0; padding: 0; box-sizing: border-box; }
  html, body { width: 920px; height: 1200px; overflow: hidden; background: var(--stage); }
  .canvas { position: relative; width: 920px; height: 1200px; background: var(--stage); font-family: "Arimo", Arial, sans-serif; color: var(--brand-blue); }

  /* Front */
  .card-front { position: absolute; left: 91px; top: 23px; width: 724px; height: 561px; background: var(--panel-grey); overflow: hidden; }
  .hero-photo { position: absolute; left: 0; top: 0; width: 724px; height: 345px;
    background:
      radial-gradient(ellipse 150px 95px at 230px 130px, rgba(226,185,160,0.95), rgba(226,185,160,0) 100%),
      radial-gradient(ellipse 130px 110px at 140px 160px, rgba(236,203,182,0.95), rgba(236,203,182,0) 100%),
      radial-gradient(ellipse 90px 60px at 40px 110px, rgba(214,170,146,0.8), rgba(214,170,146,0) 100%),
      radial-gradient(ellipse 110px 80px at 60px 300px, rgba(255,255,255,0.95), rgba(255,255,255,0) 100%),
      linear-gradient(90deg, #ebe6e2 0%, var(--linen) 30%, #f3f3f3 48%, var(--panel-grey) 62%); }
  .front-band { position: absolute; left: 0; top: 0; width: 724px; height: 561px; }
  .headline { position: absolute; right: 37px; top: 88px; text-align: right; font-family: "Roboto", Arial, sans-serif; font-weight: 300; color: var(--brand-blue); line-height: 1; }
  .headline .line-caring { display: block; font-size: 70px; letter-spacing: 1px; }
  .headline .line-for { display: block; font-size: 46px; font-weight: 400; margin-top: 6px; }
  .headline .line-matter { display: block; font-size: 81px; margin-top: 2px; }
  .front-info { position: absolute; left: 0; top: 382px; width: 724px; text-align: center; }
  .agency-name { font-family: "Tinos", "Times New Roman", serif; font-style: italic; font-weight: 700; color: var(--brand-blue); }
  .front-info .agency-name { font-size: 36px; line-height: 40px; }
  .schedule-note { font-size: 19.5px; margin-top: 14px; }
  .phone-line { font-size: 29px; margin-top: 2px; }
  .phone-line b { font-weight: 700; }
  .phone-line .gap { display: inline-block; width: 16px; }
  .address { font-size: 19px; line-height: 20px; margin-top: 9px; }

  /* Back */
  .card-back { position: absolute; left: 89px; top: 610px; width: 724px; height: 560px; background: var(--paper); overflow: hidden; }
  .intro-panel { position: absolute; left: 0; top: 0; width: 544px; height: 178px; background: var(--panel-grey); }
  .services-panel { position: absolute; left: 0; top: 178px; width: 349px; height: 216px; background: var(--panel-grey); }
  .back-title { position: absolute; left: 36px; top: 32px; font-size: 27px; white-space: nowrap; }
  .intro-text { position: absolute; left: 38px; top: 83px; width: 479px; font-size: 16px; line-height: 19.4px; text-align: justify; }
  .services { position: absolute; left: 39px; top: 193px; }
  .services h2 { font-size: 16.2px; font-weight: 700; margin-bottom: 1px; }
  .services ul { list-style: none; font-size: 14.3px; line-height: 17.2px; }
  .services li { display: flex; align-items: center; gap: 3px; }
  .services svg { width: 12px; height: 11px; flex: none; }
  .call-band { position: absolute; left: 0; top: 394px; width: 349px; height: 68px; background: var(--brand-blue); color: var(--paper); padding: 9px 0 0 38px; font-size: 16.2px; line-height: 17.6px; }
  .call-band b { font-weight: 700; }
  .stamp-box { position: absolute; left: 580px; top: 43px; width: 95px; height: 109px; border: 1px solid #b9b9b9; padding: 27px 0 0 23px; font-family: "Roboto", Arial, sans-serif; font-weight: 300; font-size: 19px; line-height: 21.5px; color: var(--stamp-grey); }
  .address-line { position: absolute; left: 384px; width: 297px; height: 1px; background: var(--rule); }
</style>
</head>
<body>
<div class="canvas">

  <section class="card-front">
    <div class="hero-photo" role="img" aria-label="Photo of a caregiver's hands gently holding an elderly person's hand on white bed linen"></div>
    <svg class="front-band" viewBox="0 0 724 561" aria-hidden="true">
      <path d="M0 320 C 200 322 450 340 724 292 L724 561 L0 561 Z" fill="var(--pale-blue)"/>
      <path d="M0 320 C 200 322 450 340 724 292 L724 300 C 520 345 300 335 0 322 Z" fill="#ffffff"/>
      <path d="M200 322 C 420 332 560 352 724 320 L724 368 C 560 385 420 350 200 322 Z" fill="var(--deep-blue)" opacity="0.85"/>
      <path d="M240 326 C 440 340 590 350 724 308 L724 330 C 580 372 430 346 240 326 Z" fill="var(--brand-blue)"/>
      <path d="M300 330 C 470 344 610 340 724 296 L724 312 C 610 356 470 346 300 330 Z" fill="#58b9e6"/>
    </svg>
    <h1 class="headline">
      <span class="line-caring">CARING</span>
      <span class="line-for">FOR THOSE THAT</span>
      <span class="line-matter">MATTER</span>
    </h1>
    <div class="front-info">
      <p class="agency-name">Gentle Hearthkeeper &amp; Helper Agency</p>
      <p class="schedule-note">To schedule an appointment, please call:</p>
      <p class="phone-line">Cell: <b>203-555-0187</b><span class="gap"></span>Office: <b>2035550142</b></p>
      <p class="address">Gentle Hearthkeeper and Helper Agency<br>48 WILLOW LANE BROOKFIELD CT 06804 US</p>
    </div>
  </section>

  <section class="card-back">
    <div class="intro-panel"></div>
    <div class="services-panel"></div>
    <p class="agency-name back-title">Gentle Hearthkeeper &amp; Helper Agency</p>
    <p class="intro-text">Gentle Hearthkeeper &amp; Helper Agency, assist elderly clients who need assistance in or out of the home. Our home care services to our clients to assist them to lead dignified and independent lives in the comfort and safety of there own homes</p>
    <div class="services">
      <h2>Our Services</h2>
      <ul>
        <li><svg viewBox="0 0 12 11"><path d="M1 6 L4.5 9.5 L11 1" fill="none" stroke="var(--brand-blue)" stroke-width="2"/></svg>Assistance with Daily Living</li>
        <li><svg viewBox="0 0 12 11"><path d="M1 6 L4.5 9.5 L11 1" fill="none" stroke="var(--brand-blue)" stroke-width="2"/></svg>Light cooking</li>
        <li><svg viewBox="0 0 12 11"><path d="M1 6 L4.5 9.5 L11 1" fill="none" stroke="var(--brand-blue)" stroke-width="2"/></svg>Light Housekeeping</li>
        <li><svg viewBox="0 0 12 11"><path d="M1 6 L4.5 9.5 L11 1" fill="none" stroke="var(--brand-blue)" stroke-width="2"/></svg>Running errands</li>
        <li><svg viewBox="0 0 12 11"><path d="M1 6 L4.5 9.5 L11 1" fill="none" stroke="var(--brand-blue)" stroke-width="2"/></svg>Accompaniment to Doctors visits</li>
        <li><svg viewBox="0 0 12 11"><path d="M1 6 L4.5 9.5 L11 1" fill="none" stroke="var(--brand-blue)" stroke-width="2"/></svg>Laundry</li>
        <li><svg viewBox="0 0 12 11"><path d="M1 6 L4.5 9.5 L11 1" fill="none" stroke="var(--brand-blue)" stroke-width="2"/></svg>In and out home activities</li>
        <li><svg viewBox="0 0 12 11"><path d="M1 6 L4.5 9.5 L11 1" fill="none" stroke="var(--brand-blue)" stroke-width="2"/></svg>Medication reminders</li>
        <li><svg viewBox="0 0 12 11"><path d="M1 6 L4.5 9.5 L11 1" fill="none" stroke="var(--brand-blue)" stroke-width="2"/></svg>Hours of services range from 4 hrs to</li>
        <li><svg viewBox="0 0 12 11"><path d="M1 6 L4.5 9.5 L11 1" fill="none" stroke="var(--brand-blue)" stroke-width="2"/></svg>Live-in services</li>
      </ul>
    </div>
    <div class="call-band">
      To schedule an appointment, please call:<br>
      Office - <b>203-555-0142)</b><br>
      <b>Cell - 203-555-0187</b>
    </div>
    <div class="stamp-box">Place<br>Stamp<br>Here</div>
    <div class="address-line" style="top:267px"></div>
    <div class="address-line" style="top:326px"></div>
    <div class="address-line" style="top:388px"></div>
  </section>

</div>
</body>
</html>
```